添付は昨年のフォーマットです。
悪くはないのですが製本してパンフレットになると文字サイズなどのバランスが悪く・・・。
今年のフォーマットをお願いしたい。
添付のフォーマットの情報を網羅してデザイン願います。
• イラストレーター形式 (.ai)

ご提案ありがとうございました!
フォーマット原稿の性質上、シンプルで流し込みしやすいデザインを選ばせてもらいました。

皆様、ご提案ありがとうございました!
どれを選んでも問題ないフォーマットでした。
今後もまた提案よろしくお願いします。

```html
<!DOCTYPE html>
<html lang="ja">
<head>
<meta charset="utf-8">
<title>北陵学園大学 学校紹介フォーマット</title>
<link href="https://fonts.googleapis.com/css2?family=Noto+Sans+JP:wght@400;500;700;900&family=Noto+Serif+JP:wght@700&display=swap" rel="stylesheet">
<style>
  :root{
    --navy:#1e3f8f;
    --navy-dark:#17306e;
    --sky:#d7e3f4;
    --sky-line:#9fb7de;
    --accent:#d2283a;
    --ink:#333;
    --gray:#ececec;
    --gray-text:#999;
  }
  *{margin:0;padding:0;box-sizing:border-box}
  html,body{width:848px;height:1200px;overflow:hidden;background:#fff}
  body{font-family:"Noto Sans JP",sans-serif;color:var(--ink);position:relative}
  .band{height:26px;background:var(--navy)}
  .band.bottom{position:absolute;left:0;right:0;bottom:0}
  .page{padding:0 40px}
  .masthead{height:96px;display:flex;align-items:center;justify-content:center;gap:18px}
  .masthead .mark{width:38px;height:38px;background:var(--accent)}
  .masthead .name{font-family:"Noto Serif JP",serif;font-weight:700;font-size:56px;letter-spacing:.12em;color:var(--navy)}
  .contact{display:flex;height:30px;align-items:center;background:var(--sky);font-size:14px;font-weight:500;color:var(--navy-dark)}
  .contact .label{background:var(--navy);color:#fff;height:100%;display:flex;align-items:center;padding:0 14px;font-weight:700;font-size:13px}
  .contact .addr{padding-left:18px;flex:1}
  .contact .tel{padding-right:18px;font-weight:700;font-size:15px}
  .faculties{display:grid;grid-template-columns:repeat(5,1fr);gap:4px;margin-top:6px}
  .faculties div{background:var(--sky);font-size:12px;padding:7px 8px;color:var(--ink)}
  .visual{margin-top:14px;height:262px;background:var(--gray);display:flex;align-items:flex-end;justify-content:center;padding-bottom:10px;font-size:11px;color:var(--gray-text)}
  .appeal{display:grid;grid-template-columns:1fr 1fr;gap:28px;margin-top:16px}
  .appeal h2{background:var(--navy);color:#fff;font-size:15px;font-weight:700;text-align:center;padding:5px 0}
  .points{list-style:none;margin-top:10px}
  .points li{font-size:20px;font-weight:900;color:var(--navy-dark);display:flex;align-items:center;gap:10px;line-height:1.6}
  .points li::before{content:"";width:9px;height:16px;background:var(--navy)}
  .residence .head{display:flex;justify-content:space-between;align-items:flex-end;border-bottom:2px solid var(--navy);padding-bottom:3px}
  .residence .head b{font-size:14px;color:var(--navy);background:var(--sky);padding:3px 10px}
  .residence .head small{font-size:10px;color:#666}
  .residence p{font-size:13px;font-weight:500;line-height:2;border-bottom:1px dashed var(--sky-line);padding:1px 4px;color:var(--ink)}
  .sections{display:grid;grid-template-columns:1fr 1fr;column-gap:28px;row-gap:18px;margin-top:22px}
  .sections h3{font-size:22px;font-weight:900;color:var(--navy);border-left:8px solid var(--navy);padding-left:10px;line-height:1.1;padding-bottom:6px;border-bottom:1px solid var(--sky-line)}
  .sections p{font-size:12.5px;line-height:1.85;margin-top:8px;text-align:justify}
  .message{margin-top:22px;display:flex;border:2px solid var(--navy);height:100px}
  .message .title{background:var(--navy);color:#fff;font-weight:900;font-size:17px;line-height:1.35;display:flex;align-items:center;padding:0 16px;width:150px}
  .message .body{flex:1;font-size:12px;line-height:1.8;padding:12px 16px}
  .message .staff{width:150px;display:flex;align-items:center;gap:8px;padding:0 10px;background:var(--sky)}
  .message .staff span{font-size:11px;font-weight:700;color:var(--navy)}
  .message .staff .photo{width:60px;height:72px;background:#cfcfcf;margin-left:auto}
</style>
</head>
<body>
  <div class="band"></div>
  <main class="page">
    <header class="masthead">
      <div class="mark"></div>
      <div class="name">北陵学園大学</div>
    </header>

    <div class="contact">
      <span class="label">問い合わせ先</span>
      <span class="addr">〒000-0000　架空県みどり市桜台3丁目12番地　入試広報課</span>
      <span class="tel">TEL：012-345-6789</span>
    </div>

    <div class="faculties">
      <div>●●●●学部／●●●●学科</div><div>●●●●学部／●●●●学科</div><div>●●●●学部／●●●●学科</div><div>●●●●学部／●●●●学科</div><div>●●●●学部／●●●●学科</div>
      <div>●●●●学部／●●●●学科</div><div>●●●●学部／●●●●学科</div><div>●●●●学部／●●●●学科</div><div>●●●●学部／●●●●学科</div><div>●●●●学部／●●●●学科</div>
    </div>

    <div class="visual" role="img" aria-label="キャンパスのイメージビジュアル">イメージビジュアルエリア</div>

    <section class="appeal">
      <div>
        <h2>北陵学園大学のここが魅力</h2>
        <ul class="points">
          <li>学力優秀者奨学金制度あり</li>
          <li>教員採用試験 123 名合格（昨年度）</li>
          <li>管理栄養士合格率 96.5％！</li>
        </ul>
      </div>
      <div class="residence">
        <div class="head"><b>沖縄県出身在籍者の現住所内訳</b><small>2023年5月現在</small></div>
        <p>那覇市 5名／名護市 3名／沖縄市 2名／浦添市 2名</p>
        <p>宜野湾市 2名／糸満市 1名／うるま市 1名／豊見城市 1名</p>
        <p>石垣市 1名／宮古島市 1名／南城市 1名</p>
      </div>
    </section>

    <section class="sections">
      <article>
        <h3>学びについて</h3>
        <p>本学では「生活」を科学の視点で捉え、実践的な学びを大切にしています。少人数制の授業と充実した実験・実習設備により、専門知識と技能を確実に身につけることができます。学部の枠を越えた連携授業も多く、幅広い視野を持った人材を育てます。</p>
      </article>
      <article>
        <h3>環境について</h3>
        <p>緑豊かなキャンパスは最寄り駅から徒歩圏内にあり、通学にも便利です。図書館や学生ラウンジ、最新の実習室を備え、学生が自主的に学べる環境を整えています。周辺には生活に必要な施設もそろい、一人暮らしの学生も安心して過ごせます。</p>
      </article>
      <article>
        <h3>学生生活について</h3>
        <p>部活動やサークル、学園祭などの行事を通じて、学年や学部を越えた交流が生まれています。学生寮や奨学金制度のほか、学生相談室によるきめ細かなサポートも用意しています。地域のボランティア活動に参加する学生も多く、充実した日々を送っています。</p>
      </article>
      <article>
        <h3>就職支援について</h3>
        <p>入学直後からキャリア教育を実施し、一人ひとりの希望に合わせた支援を行っています。専任スタッフによる個別面談や模擬面接、企業説明会を学内で開催し、毎年高い就職率を実現しています。資格取得のための対策講座も充実しています。</p>
      </article>
    </section>

    <aside class="message">
      <div class="title">大学担当者から<br>メッセージ</div>
      <div class="body">県外からの入学も多く、同郷の先輩が多数在籍しています。本学で学ぶ皆さんを教職員一同全力で応援します。オープンキャンパスでお会いできるのを楽しみにしています。</div>
      <div class="staff"><span>担当者名入</span><div class="photo" role="img" aria-label="担当者の写真"></div></div>
    </aside>
  </main>
  <div class="band bottom"></div>
</body>
</html>
```